Corporate Design für Sweet Table-Service
Zielgruppe
Zwei Ladys - die eine Besitzerin eines etablierten Cafés, die andere Inhaberin eines Cake Pops-Service - wagen die gemeinsame Geschäftsgründung: Einen Service für Sweet Tables und Candy Bars. Vor allem in der Hochzeitsszene sind diese Begriffe fest etabliert. Dabei handelt es sich um eine neue Interpretation des Dessertbüffets. Die Besonderheit: Die Leckereien werden nicht einfach nur auf einem Tisch platziert, sondern der Tisch wird mit sehr viel Liebe zum Detail dekoriert und fügt sich perfekt in das Thema der Feier ein, stilistisch wie farblich. Unser Service erstreckt sich von selbst hergestellten Leckereien inklusive Cake Pops, Cupcakes, Kuchen und Torten über herkömmliche Süßigkeiten bis hin zur passenden Papeterie (inklusive Anlieferung, Aufbau und Dekoration vor Ort sowie Abholung). Der Kunde erhält also alles aus einer Hand. Und das Besondere an unserem Konzept ist, dass unser Sortiment nicht beim Süßen endet, sondern dass wir auch Pikantes anbieten. Daher auch der Name Lark'n'Lore. Wir laden Euch ein paar Fotos von Sweet Tables/Candy Bars hoch, damit Ihr einen Eindruck bekommt. Unser Internetauftritt steht schon ziemlich, befindet sich aber noch im Arbeitsmodus. Link: feierfee-muenchen.baukastenweb.com. Zur Info: Die Fotos/das Logo dienen lediglich als Platzhalter und die Domain 'larknlore.de' muss noch käuflich erworben werden.
Aufgabenstellung
Wir wünschen uns ein Corporate Design in unseren Unternehmensfarben Brombeere (rgb 77, 15, 48) und Apfelgrün (rgb 130, 185, 36). Das Logo stellen wir uns von der Form her rechteckig oder oval vor. Vom Stil her elegant und gerne auch ein wenig verspielt, aber bitte keine comicartigen Designs. Wir benötigen außerdem noch einen Untertitel/Slogan in Form von ein paar Schlagwörtern, die unseren Service beschreiben und sind für Vorschläge dankbar. Der Begriff Candy Bar sollte darin eher nicht vorkommen, da er sich für uns wenig hochwertig anhört. Das Corporate Design sollte Logo, Briefpapier und Visitenkarten umfassen. Wir freuen uns sehr auf Eure Entwürfe und sind sehr gespannt. Herzlichen Dank für Eure Arbeit!

```html
<!DOCTYPE html>
<html lang="de">
<head>
<meta charset="utf-8">
<title>Lark'n'Lore – Briefpapier</title>
<link rel="stylesheet" href="https://fonts.googleapis.com/css2?family=Quicksand:wght@400;500;700&display=swap">
<style>
  :root {
    --brombeere: #4d0f30;
    --apfelgruen: #82b924;
    --text-grey: #6a5a63;
    --paper: #ffffff;
    --backdrop: #e9e5ea;
    --pattern-tint: #f1eff1;
  }
  * { box-sizing: border-box; margin: 0; padding: 0; }
  html, body {
    width: 1200px; height: 899px; overflow: hidden;
    background: var(--backdrop);
    font-family: "Quicksand", sans-serif;
    color: var(--brombeere);
  }
  .letterhead {
    position: absolute; left: 296px; top: 20px;
    width: 608px; height: 859px;
    background: var(--paper);
    box-shadow: 0 4px 18px rgba(60, 40, 60, 0.12);
    overflow: hidden;
  }
  .brand-name {
    position: absolute; left: 56px; top: 40px;
    font-size: 26px; font-weight: 700; color: var(--brombeere);
    display: flex; align-items: center; gap: 8px;
  }
  .brand-name .dot {
    width: 10px; height: 10px; border-radius: 50%; background: var(--apfelgruen);
  }
  .sender-line {
    position: absolute; left: 56px; top: 146px;
    font-size: 7.5px; color: var(--brombeere);
  }
  .sender-line strong { font-weight: 700; }
  .contact-block {
    position: absolute; left: 398px; top: 40px;
    font-size: 8px; line-height: 1.35;
  }
  .contact-block .company { font-weight: 700; }
  .contact-block .owners { color: var(--apfelgruen); font-weight: 700; }
  .contact-block .address { margin-top: 12px; }
  .contact-row { display: flex; align-items: center; gap: 6px; }
  .contact-row svg { width: 8px; height: 8px; flex: none; }
  .contact-group { margin-top: 10px; }
  .web { font-weight: 700; }
  .fold-mark {
    position: absolute; left: 0; width: 14px; height: 1px;
    background: var(--apfelgruen);
  }
  .fold-mark.upper { top: 305px; }
  .fold-mark.punch { top: 430px; }
  .fold-mark.lower { top: 610px; }
  .footer-texture {
    position: absolute; left: 0; right: 0; bottom: 0; height: 95px;
    background: linear-gradient(to bottom, rgba(241,239,241,0), var(--pattern-tint) 45%);
  }
  .footer {
    position: absolute; left: 56px; right: 40px; bottom: 26px;
    display: flex; justify-content: space-between;
    font-size: 6.2px; line-height: 1.4; color: var(--text-grey);
  }
  .footer .label { color: var(--apfelgruen); font-weight: 700; }
</style>
</head>
<body>
  <main class="letterhead">
    <div class="brand-name"><span class="dot"></span>Lark'n'Lore</div>

    <p class="sender-line"><strong>Lark'n'Lore</strong> · Amselweg 42 · 80939 München</p>

    <section class="contact-block">
      <p class="company">Lark'n'Lore</p>
      <p class="owners">Clara Brandt &amp; Nele Weiss</p>
      <p class="address">Amselweg 42<br>80939 München</p>
      <div class="contact-group">
        <p class="contact-row">
          <svg viewBox="0 0 10 10"><path d="M2 1 L4 3 L3 4 Q4 6 6 7 L7 6 L9 8 L8 9 Q3 9 1 2 Z" fill="none" stroke="var(--apfelgruen)" stroke-width="0.9"/></svg>
          CB +49 (0)170 55512340</p>
        <p class="contact-row">
          <svg viewBox="0 0 10 10"><path d="M2 1 L4 3 L3 4 Q4 6 6 7 L7 6 L9 8 L8 9 Q3 9 1 2 Z" fill="none" stroke="var(--apfelgruen)" stroke-width="0.9"/></svg>
          NW +49 (0)151 55598761</p>
      </div>
      <div class="contact-group">
        <p class="contact-row">
          <svg viewBox="0 0 10 10"><rect x="1" y="2.5" width="8" height="5.5" fill="none" stroke="var(--apfelgruen)" stroke-width="0.9"/><path d="M1 2.5 L5 5.5 L9 2.5" fill="none" stroke="var(--apfelgruen)" stroke-width="0.9"/></svg>
          service@larknlore.de</p>
        <p class="contact-row web">
          <svg viewBox="0 0 10 10"><path d="M1.5 5 L5 1.5 L8.5 5 M2.5 4.5 V8.5 H7.5 V4.5" fill="none" stroke="var(--apfelgruen)" stroke-width="0.9"/></svg>
          www.larknlore.de</p>
      </div>
    </section>

    <span class="fold-mark upper"></span>
    <span class="fold-mark punch"></span>
    <span class="fold-mark lower"></span>

    <div class="footer-texture" role="img" aria-label="Dezentes Wortmuster mit Schlagwörtern des Sweet-Table-Service"></div>

    <footer class="footer">
      <div>
        <span class="label">GF:</span> Clara Brandt &amp; Nele Weiss<br>
        <span class="label">USt.-ID:</span> DE 123 456 789<br>
        <span class="label">Amtsgericht Musterburg:</span> HRA 12345
      </div>
      <div>
        <span class="label">Stadtbank München</span><br>
        IBAN DE00000000 0000 0000 0000 00<br>
        BIC XXXXXXXXXXX
      </div>
      <div>
        <span class="label">Kreisbank München</span><br>
        IBAN DE00000000 0000 0000 0000 00<br>
        BIC XXXXXXXXXXX
      </div>
      <div>
        <span class="label">Isar Sparkasse München</span><br>
        IBAN DE00000000 0000 0000 0000 00<br>
        BIC XXXXXXXXXXX
      </div>
    </footer>
  </main>
</body>
</html>
```